New business stationairy

I need paper with header and footer and business cards.
I am a Ltd Company and my main field of expertise is QA/QC inspection in the Oil and Gas Industry. I will need all contact detail inserted and a footer with registration number and bank details etc

Industry/Entity Type

Business

```html
<!DOCTYPE html>
<html lang="en">
<head>
<meta charset="utf-8">
<title>Halden Inspection Services Ltd – Stationery</title>
<link href="https://fonts.googleapis.com/css2?family=Nunito:wght@700&family=Play:wght@700&family=Roboto+Condensed:wght@300;400&display=swap" rel="stylesheet">
<style>
  :root {
    --navy: #253a7c;
    --navy-soft: #c8cde0;
    --navy-faint: #e7eaf2;
    --paper: #ffffff;
    --backdrop: #8c8c8c;
  }
  * { margin: 0; padding: 0; box-sizing: border-box; }
  html, body { width: 1200px; height: 1000px; overflow: hidden; }
  body { background: var(--backdrop); position: relative; }

  .sheet { position: absolute; background: var(--paper); overflow: hidden; }
  .sheet svg.wave { position: absolute; left: 0; bottom: 0; }

  .brand-name {
    font-family: "Nunito", sans-serif; font-weight: 700; color: var(--navy);
    position: absolute; white-space: nowrap; letter-spacing: -0.2px;
  }
  .brand-dot { position: absolute; border-radius: 50%; background: var(--navy); }
  .faint-disc { position: absolute; border-radius: 50%; }

  /* Letterhead */
  .letterhead { left: 34px; top: 83px; width: 612px; height: 793px; }
  .letterhead .brand-dot { left: 111px; top: 32px; width: 66px; height: 66px; }
  .letterhead .brand-name { left: 48px; top: 98px; font-size: 14.5px; }
  .letterhead .faint-disc { left: 153px; top: 300px; width: 306px; height: 280px; background: var(--navy-faint); }
  .letter-footer {
    position: absolute; top: 692px; left: 0; width: 612px;
    font-family: "Roboto Condensed", sans-serif; font-weight: 400; font-size: 8px; color: var(--navy);
  }
  .letter-footer .address { position: absolute; right: 441px; top: 5px; text-align: right; line-height: 12px; }
  .letter-footer .divider { position: absolute; left: 179px; top: 0; width: 1px; height: 30px; background: var(--navy); }
  .letter-footer .contact { position: absolute; left: 188px; top: 5px; line-height: 12px; }
  .contact-line { display: flex; align-items: center; gap: 5px; }
  .contact-line svg { flex: none; }

  /* Cards */
  .card { width: 419px; height: 277px; left: 701px; }
  .card-personal { top: 202px; }
  .card-brand { top: 520px; }

  .card-personal .person-name {
    position: absolute; left: 186px; top: 33px;
    font-family: "Play", sans-serif; font-weight: 700; font-size: 25px; color: var(--navy);
  }
  .card-personal .person-role {
    position: absolute; left: 187px; top: 60px;
    font-family: "Roboto Condensed", sans-serif; font-size: 11px; color: #555;
  }
  .card-personal .faint-disc { left: 242px; top: 101px; width: 196px; height: 170px; background: var(--navy-soft); }
  .card-contacts {
    position: absolute; left: 40px; top: 152px;
    font-family: "Roboto Condensed", sans-serif; font-weight: 300; font-size: 12.5px; color: #444;
  }
  .card-contacts .contact-line { gap: 9px; margin-bottom: 6px; align-items: flex-start; line-height: 13px; }
  .card-contacts .contact-line span { padding-top: 1px; }

  .card-brand .brand-dot { left: 143px; top: 60px; width: 132px; height: 120px; }
  .card-brand .brand-name { left: 0; width: 419px; text-align: center; top: 181px; font-size: 24.5px; }
</style>
</head>
<body>

<section class="sheet letterhead" aria-label="Letterhead">
  <div class="brand-dot"></div>
  <div class="brand-name">Halden Inspection Services Ltd</div>
  <div class="faint-disc"></div>

  <footer class="letter-footer">
    <div class="address">The Willows, Mill Lane, Ashford,<br>Eastbrook, Somerset, TA9 4XY</div>
    <div class="divider"></div>
    <div class="contact">
      <div class="contact-line">
        <svg width="9" height="9" viewBox="0 0 10 10"><rect width="10" height="10" rx="1.5" fill="#253a7c"/><rect x="3" y="1.8" width="4" height="6.4" rx="0.6" fill="none" stroke="#fff" stroke-width="0.9"/></svg>
        <span>07700 900418</span>
      </div>
      <div class="contact-line">
        <svg width="9" height="9" viewBox="0 0 10 10"><rect width="10" height="10" rx="1.5" fill="#253a7c"/><rect x="2" y="3" width="6" height="4.4" fill="none" stroke="#fff" stroke-width="0.8"/><path d="M2 3l3 2.4L8 3" fill="none" stroke="#fff" stroke-width="0.8"/></svg>
        <span>mhalden@example.co.uk</span>
      </div>
    </div>
  </footer>

  <svg class="wave" width="612" height="60" viewBox="0 0 612 60">
    <path d="M0 3 C150 -6 330 6 460 26 C520 34 570 32 612 18 L612 22 C560 38 500 40 440 34 C300 18 150 12 0 14 Z" fill="#c8cde0"/>
    <path d="M0 26 C160 18 320 30 440 42 C520 48 575 40 612 8 L612 60 L0 60 Z" fill="#253a7c"/>
  </svg>
</section>

<section class="sheet card card-personal" aria-label="Business card, contact side">
  <div class="faint-disc"></div>
  <div class="person-name">Maren Halden</div>
  <div class="person-role">Owner</div>

  <div class="card-contacts">
    <div class="contact-line">
      <svg width="15" height="15" viewBox="0 0 10 10"><rect width="10" height="10" rx="1.5" fill="#253a7c"/><rect x="3" y="1.8" width="4" height="6.4" rx="0.6" fill="none" stroke="#fff" stroke-width="0.8"/><circle cx="5" cy="7.1" r="0.5" fill="#fff"/></svg>
      <span>07700 900418</span>
    </div>
    <div class="contact-line">
      <svg width="15" height="15" viewBox="0 0 10 10"><rect width="10" height="10" rx="1.5" fill="#253a7c"/><rect x="2" y="3" width="6" height="4.4" fill="none" stroke="#fff" stroke-width="0.7"/><path d="M2 3l3 2.4L8 3" fill="none" stroke="#fff" stroke-width="0.7"/></svg>
      <span>mhalden@example.co.uk</span>
    </div>
    <div class="contact-line">
      <svg width="15" height="15" viewBox="0 0 10 10"><rect width="10" height="10" rx="1.5" fill="#253a7c"/><path d="M5 1.8a2.3 2.3 0 0 1 2.3 2.3C7.3 6 5 8.4 5 8.4S2.7 6 2.7 4.1A2.3 2.3 0 0 1 5 1.8z" fill="#fff"/><circle cx="5" cy="4.1" r="0.9" fill="#253a7c"/></svg>
      <span>The Willows, Mill Lane, Ashford<br>Eastbrook, Somerset, TA9 4XY</span>
    </div>
  </div>

  <svg class="wave" width="419" height="42" viewBox="0 0 419 42">
    <path d="M0 3 C90 -2 200 6 270 22 C320 32 370 30 419 16 L419 20 C370 34 320 36 260 28 C180 14 90 10 0 12 Z" fill="#c8cde0"/>
    <path d="M0 18 C110 12 200 18 260 26 C330 34 380 24 419 6 L419 42 L0 42 Z" fill="#253a7c"/>
  </svg>
</section>

<section class="sheet card card-brand" aria-label="Business card, brand side">
  <div class="brand-dot"></div>
  <div class="brand-name">Halden Inspection Services Ltd</div>

  <svg class="wave" width="419" height="42" viewBox="0 0 419 42">
    <path d="M0 3 C90 -2 200 6 270 22 C320 32 370 30 419 16 L419 20 C370 34 320 36 260 28 C180 14 90 10 0 12 Z" fill="#c8cde0"/>
    <path d="M0 18 C110 12 200 18 260 26 C330 34 380 24 419 6 L419 42 L0 42 Z" fill="#253a7c"/>
  </svg>
</section>

</body>
</html>
```